Business Card Design

We are a state licensed general contractor on the south east coast of Florida. We are a remodeling and home repairs business that have been in business for 14 years. Since we are located on the coast and our business name is Ridgeway Builders of Lower Meadow, Inc, we would like a "Ridgeway" themed design that would appeal to more affluent customers. I would like to see light blue colors with waves incorporated into the design. I would also like the design to communicate a modern, confident, responsible company character.

Industry/Entity Type

Contractor

Contact Information for Business Card

Tim Harlow 555-276-3148

```html
<!DOCTYPE html>
<html lang="en">
<head>
<meta charset="utf-8">
<title>Ridgeway Builders – Business Card</title>
<link rel="stylesheet" href="https://fonts.googleapis.com/css2?family=Open+Sans:wght@400;600;700&display=swap">
<style>
  :root {
    --backdrop: #e9e6e1;
    --card: #ffffff;
    --brand-blue: #1f5fa8;
    --band-top: #2f6fb6;
    --band-bottom: #1c57a0;
    --ink-light: #ffffff;
    --rule: #1d5aa3;
  }
  * { margin: 0; padding: 0; box-sizing: border-box; }
  html, body { width: 1200px; height: 818px; overflow: hidden; }
  body {
    background: var(--backdrop);
    font-family: "Open Sans", Arial, sans-serif;
    position: relative;
  }
  .card {
    position: absolute;
    left: 100px; top: 123px;
    width: 1000px; height: 572px;
    background: var(--card);
    box-shadow: 0 10px 30px rgba(0,0,0,0.18);
    overflow: hidden;
  }
  .brand {
    position: absolute;
    left: 90px; top: 170px;
    display: flex; align-items: center; gap: 18px;
  }
  .brand-dot {
    width: 34px; height: 34px; border-radius: 50%;
    background: var(--brand-blue);
  }
  .brand-name {
    font-size: 78px; font-weight: 600; color: var(--brand-blue);
    line-height: 1;
  }
  .owner {
    position: absolute;
    left: 610px; top: 70px;
    color: var(--brand-blue);
  }
  .owner-name { font-size: 44px; font-weight: 700; letter-spacing: 0.5px; line-height: 1; }
  .owner-role { font-size: 30px; font-weight: 600; line-height: 1.05; }
  .band {
    position: absolute;
    left: 0; top: 300px;
    width: 100%; height: 180px;
    background: linear-gradient(180deg, var(--band-top), var(--band-bottom));
  }
  .band::before, .band::after {
    content: ""; position: absolute; left: 0; right: 0; height: 2px;
    background: var(--ink-light); opacity: 0.85;
  }
  .band::before { top: 9px; }
  .band::after { bottom: 9px; }
  .band-rule {
    position: absolute; left: 0; right: 0; top: 494px; height: 2px;
    background: var(--rule);
  }
  .contact {
    position: absolute;
    list-style: none;
    color: var(--ink-light);
    font-size: 27px; line-height: 40px;
  }
  .contact li { display: flex; align-items: center; gap: 14px; }
  .contact svg { width: 20px; height: 20px; flex: none; fill: var(--ink-light); }
  .contact-phones { left: 320px; top: 332px; }
  .contact-location { left: 600px; top: 332px; }
  .contact-location .indent { padding-left: 34px; }
</style>
</head>
<body>
  <article class="card">
    <div class="brand">
      <span class="brand-dot"></span>
      <span class="brand-name">Ridgeway</span>
    </div>

    <div class="owner">
      <p class="owner-name">TIM HARLOW</p>
      <p class="owner-role">owner</p>
    </div>

    <div class="band"></div>
    <div class="band-rule"></div>

    <ul class="contact contact-phones">
      <li>
        <svg viewBox="0 0 20 20" aria-hidden="true"><path d="M6 1h8a1.5 1.5 0 0 1 1.5 1.5v15A1.5 1.5 0 0 1 14 19H6a1.5 1.5 0 0 1-1.5-1.5v-15A1.5 1.5 0 0 1 6 1zm0 2v12h8V3zm4 13.2a1 1 0 1 0 0 2 1 1 0 0 0 0-2z"/></svg>
        555-276-3148
      </li>
      <li>
        <svg viewBox="0 0 20 20" aria-hidden="true"><path d="M5 2l3 4-2 2c1 2.5 3.5 5 6 6l2-2 4 3-2 3C9 18 2 11 2 4z"/></svg>
        555-302.4418
      </li>
      <li>
        <svg viewBox="0 0 20 20" aria-hidden="true"><path d="M5 1h8l2 2v4H5zM2 8h16a1 1 0 0 1 1 1v7a1 1 0 0 1-1 1h-2v2H4v-2H2a1 1 0 0 1-1-1V9a1 1 0 0 1 1-1zm4 6v3h8v-3z"/></svg>
        555-302.7791
      </li>
    </ul>

    <ul class="contact contact-location">
      <li>
        <svg viewBox="0 0 20 20" aria-hidden="true"><path d="M1 4h18v12H1zm2 2v.4l7 5 7-5V6l-7 5z"/></svg>
        ridgeway.th@mailbox.com
      </li>
      <li>
        <svg viewBox="0 0 20 20" aria-hidden="true"><path d="M10 1a6 6 0 0 1 6 6c0 4.5-6 12-6 12S4 11.5 4 7a6 6 0 0 1 6-6zm0 3.5a2.5 2.5 0 1 0 0 5 2.5 2.5 0 0 0 0-5z"/></svg>
        4820 Harlan Circle
      </li>
      <li class="indent">Lower Meadow, FL 30512</li>
    </ul>
  </article>
</body>
</html>
```